M&A Advisory firm needs elegant and powerful letterhead

We need a powerful but elegant letterhead to engage with the international financial industry.

Target Market(s)

New York and International Financial Industry

Industry/Entity Type

Finance

Font styles to use
Other font styles liked:
• Poppins

Requirements
Must have
• 482 W 71st Street 14th Floor New York, NY 10157 O: +1 (212) 555 0147 F: +1 (212) 555 0182

```html
<!DOCTYPE html>
<html lang="en">
<head>
<meta charset="UTF-8">
<title>Norvale Letterhead</title>
<link href="https://fonts.googleapis.com/css2?family=Poppins:wght@400;500&display=swap" rel="stylesheet">
<style>
  :root {
    --backdrop: #e4e5e7;
    --paper: #ffffff;
    --brand-blue: #2f6aa7;
    --band-deep: #2c6aa6;
    --band-soft: #5d74b9;
    --band-mist: #7d8fca;
    --ink: #2a2a2a;
    --tagline-grey: #8a8a8a;
    --mark-faint: #a9afd6;
  }
  * { box-sizing: border-box; margin: 0; padding: 0; }
  html, body {
    width: 1200px;
    height: 900px;
    overflow: hidden;
    background: var(--backdrop);
    font-family: "Poppins", sans-serif;
  }
  .letterhead {
    position: absolute;
    left: 267px;
    top: 20px;
    width: 666px;
    height: 860px;
    background: var(--paper);
    box-shadow: 0 6px 24px rgba(0,0,0,0.18);
    overflow: hidden;
  }
  .side-band {
    position: absolute;
    left: 0;
    top: 0;
    width: 158px;
    height: 100%;
    background: var(--band-deep);
  }
  .side-band__photo {
    position: absolute;
    left: 0;
    top: 0;
    width: 100%;
    height: 64%;
    background:
      radial-gradient(ellipse 70px 110px at 95px 190px, var(--band-mist) 0%, rgba(125,143,202,0) 100%),
      linear-gradient(180deg, var(--band-soft) 0%, var(--band-soft) 55%, var(--band-deep) 100%);
  }
  .side-band__mark {
    position: absolute;
    left: 42px;
    bottom: 52px;
    width: 74px;
    height: 74px;
    border-radius: 50%;
    background: var(--mark-faint);
    opacity: 0.75;
  }
  .margin-rule {
    position: absolute;
    left: 176px;
    top: 0;
    width: 3px;
    height: 100%;
    background: var(--brand-blue);
  }
  .brand {
    position: absolute;
    right: 30px;
    top: 46px;
    display: flex;
    align-items: center;
    gap: 14px;
  }
  .brand__dot {
    width: 30px;
    height: 30px;
    border-radius: 50%;
    background: var(--brand-blue);
  }
  .brand__text { display: flex; flex-direction: column; }
  .brand__name {
    font-weight: 400;
    font-size: 46px;
    line-height: 1;
    letter-spacing: 1px;
    color: var(--brand-blue);
  }
  .brand__tagline {
    margin-top: 4px;
    font-size: 10.5px;
    letter-spacing: 2.6px;
    color: var(--tagline-grey);
  }
  .contact {
    position: absolute;
    left: 168px;
    bottom: 26px;
    list-style: none;
  }
  .contact__item {
    display: flex;
    align-items: center;
    gap: 10px;
    height: 20px;
    margin-top: 10px;
    font-size: 11.5px;
    color: var(--ink);
  }
  .contact__icon {
    width: 20px;
    height: 20px;
    flex: none;
    border-radius: 50%;
    background: var(--brand-blue);
    display: flex;
    align-items: center;
    justify-content: center;
    box-shadow: 0 0 0 2px var(--paper);
  }
  .contact__icon svg { width: 11px; height: 11px; fill: var(--paper); }
</style>
</head>
<body>
  <main class="letterhead">
    <aside class="side-band">
      <div class="side-band__photo" role="img" aria-label="Blue-tinted photograph of banknotes under a magnifying glass"></div>
      <div class="side-band__mark"></div>
    </aside>
    <div class="margin-rule"></div>

    <header class="brand">
      <span class="brand__dot"></span>
      <div class="brand__text">
        <span class="brand__name">NORVALE</span>
        <span class="brand__tagline">Advising on the Deal</span>
      </div>
    </header>

    <ul class="contact">
      <li class="contact__item">
        <span class="contact__icon">
          <svg viewBox="0 0 12 12"><path d="M6 0.5a3.8 3.8 0 0 0-3.8 3.8C2.2 7 6 11.5 6 11.5S9.8 7 9.8 4.3A3.8 3.8 0 0 0 6 0.5zm0 5.3a1.5 1.5 0 1 1 0-3 1.5 1.5 0 0 1 0 3z"/></svg>
        </span>
        482 W 71st Street 14th Floor New York, NY 10157
      </li>
      <li class="contact__item">
        <span class="contact__icon">
          <svg viewBox="0 0 12 12"><path d="M2.6 0.8l1.8 0 0.9 2.6-1.2 1a6.5 6.5 0 0 0 3.5 3.5l1-1.2 2.6 0.9 0 1.8c0 0.6-0.5 1.1-1.1 1.1A9.6 9.6 0 0 1 1.5 1.9c0-0.6 0.5-1.1 1.1-1.1z"/></svg>
        </span>
        +1 (212) 555 0147
      </li>
      <li class="contact__item">
        <span class="contact__icon">
          <svg viewBox="0 0 12 12"><path d="M3 1h6v3H3zM1 4.5h10v4.5H9V7H3v2H1zM3.5 7.8h5V11h-5z"/></svg>
        </span>
        +1 (212) 555 0182
      </li>
    </ul>
  </main>
</body>
</html>
```